Bref créative
BRISK FIELD Stationery
Stationery for BRISKFIELD web site
Professional
Tomas Kerbrune
7 Rue Montaleur, Res. Les Pins
Vallombre
info@briskfield-exemple.com
www.briskfield-exemple.com

```html
<!DOCTYPE html>
<html lang="en">
<head>
<meta charset="utf-8">
<title>BRISK FIELD Stationery</title>
<link href="https://fonts.googleapis.com/css2?family=Titillium+Web:wght@400;700&display=swap" rel="stylesheet">
<style>
:root{
  --bg:#e9e6e2;
  --paper:#ffffff;
  --red:#c8201f;
  --red-dark:#7a1111;
  --red-deep:#4a0a0a;
  --ink:#333333;
  --grey:#8a8a8a;
  --line:#c9c9c9;
  --slate:#555555;
}
*{box-sizing:border-box;margin:0;padding:0}
html,body{width:1200px;height:326px;overflow:hidden;background:var(--bg);font-family:"Titillium Web",Arial,sans-serif;color:var(--ink)}
.stage{position:relative;width:1200px;height:326px}
.sheet{position:absolute;background:var(--paper);box-shadow:0 2px 6px rgba(0,0,0,.25);overflow:hidden}
.brand{display:flex;align-items:center;gap:4px;font-weight:700;color:var(--red);letter-spacing:.5px;white-space:nowrap;line-height:1}
.brand .dot{display:inline-block;border-radius:50%;background:var(--red)}
.brand.light{color:#fff}
.brand.light .dot{background:#fff}
.watermark{position:absolute;border-radius:50%;background:radial-gradient(circle,rgba(120,120,120,.22),rgba(120,120,120,0) 70%)}
.footer{position:absolute;left:6px;right:6px;bottom:6px;text-align:center;font-size:5px;line-height:1.2;color:var(--grey);white-space:nowrap;overflow:hidden}
.option-label{position:absolute;font-size:7px;color:var(--slate);letter-spacing:1px;white-space:nowrap}

.letterhead-a{left:44px;top:22px;width:200px;height:280px}
.letterhead-a .brand{position:absolute;left:50%;top:16px;transform:translateX(-50%);font-size:10px}
.letterhead-a .brand .dot{width:9px;height:9px}
.letterhead-a .watermark{left:40px;top:165px;width:150px;height:120px}

.letterhead-b{left:254px;top:22px;width:180px;height:280px}
.letterhead-b .brand{position:absolute;left:12px;top:16px;font-size:9px}
.letterhead-b .brand .dot{width:8px;height:8px}
.letterhead-b .watermark{left:60px;top:120px;width:150px;height:130px}
.letterhead-b .band{position:absolute;left:0;right:0;bottom:0;height:10px;background:linear-gradient(90deg,var(--red-dark),var(--red))}
.letterhead-b .footer{bottom:15px}

.fax-sheet{left:446px;top:22px;width:236px;height:280px}
.fax-sheet .topbar{position:absolute;left:0;right:0;top:0;height:6px;background:linear-gradient(90deg,var(--red-deep),var(--red))}
.fax-sheet .brand{position:absolute;left:16px;top:16px;font-size:9px}
.fax-sheet .brand .dot{width:8px;height:8px}
.fax-sheet h1{position:absolute;left:16px;top:40px;font-size:15px;line-height:1;font-weight:700;color:var(--ink)}
.fax-fields{position:absolute;left:16px;right:14px;top:64px;display:grid;grid-template-columns:1fr 1fr;column-gap:12px;row-gap:6px}
.fax-field{font-size:5px;line-height:8px;color:var(--grey);border-bottom:1px solid var(--line);height:9px}
.fax-checks{position:absolute;left:16px;right:14px;top:126px;display:flex;gap:8px;font-size:5px;line-height:6px;color:var(--grey)}
.fax-checks span::before{content:"";display:inline-block;width:4px;height:4px;border:1px solid var(--grey);margin-right:2px;vertical-align:middle}
.fax-rule{position:absolute;left:16px;right:14px;top:138px;border-top:1px solid var(--line)}

.env{position:absolute;box-shadow:0 2px 6px rgba(0,0,0,.3);overflow:hidden}
.env svg{position:absolute;left:0;top:0}
.env-back-a{left:700px;top:40px;width:230px;height:95px;background:linear-gradient(180deg,#4a4a4a,#2a2a2a)}
.env-back-b{left:952px;top:40px;width:230px;height:95px;background:linear-gradient(180deg,var(--red),var(--red-deep))}
.env-back-a .brand,.env-back-b .brand{position:absolute;left:50%;top:46px;transform:translateX(-50%);font-size:8px}
.env-back-a .brand .dot,.env-back-b .brand .dot{width:7px;height:7px}
.env-front{background:var(--paper);width:230px;height:100px;top:122px}
.env-front-a{left:712px}
.env-front-b{left:962px}
.env-front .brand{position:absolute;left:10px;top:10px;font-size:8px}
.env-front .brand .dot{width:7px;height:7px}
.env-front .band{position:absolute;left:0;right:0;bottom:0;height:8px}
.env-front-a .band{background:linear-gradient(90deg,#2a2a2a,#555)}
.env-front-b .band{background:linear-gradient(90deg,var(--red-dark),var(--red))}
.env-front .address{position:absolute;right:12px;bottom:16px;font-size:5px;color:var(--grey);text-align:right;line-height:1.5;white-space:nowrap}
.opt-a{left:790px;top:230px}
.opt-b{left:1040px;top:230px}

.card{position:absolute;top:258px;width:96px;height:54px;border-radius:3px;box-shadow:0 2px 5px rgba(0,0,0,.3);overflow:hidden;font-size:4px}
.card .brand{position:absolute;left:8px;top:20px;font-size:7px}
.card .brand .dot{width:6px;height:6px}
.card .details{position:absolute;left:8px;bottom:5px;line-height:1.4;white-space:nowrap}
.card-grey{left:700px;background:linear-gradient(180deg,#5a5a5a,#2e2e2e);color:#ddd}
.card-white{left:806px;background:var(--paper);color:var(--grey)}
.card-white .stripe{position:absolute;left:0;right:0;top:0;height:5px;background:var(--red)}
.card-red{left:912px;background:radial-gradient(circle at 50% 40%,var(--red),var(--red-deep))}
.card-dark{left:1018px;background:linear-gradient(180deg,#333,#1a1a1a);color:#ccc}
.card-red .brand{left:50%;transform:translateX(-50%)}
</style>
</head>
<body>
<main class="stage">

  <section class="sheet letterhead-a" aria-label="Letterhead option 1">
    <div class="brand"><span class="dot"></span>BRISK FIELD</div>
    <div class="watermark" role="img" aria-label="Faint brand symbol decoration"></div>
    <p class="footer">7 Rue Montaleur, Res. Les Pins · Vallombre · www.briskfield-exemple.com</p>
  </section>
  <span class="option-label" style="left:118px;top:308px">OPTION 1</span>

  <section class="sheet letterhead-b" aria-label="Letterhead option 2">
    <div class="brand"><span class="dot"></span>BRISK FIELD</div>
    <div class="watermark" role="img" aria-label="Faint brand symbol decoration"></div>
    <p class="footer">info@briskfield-exemple.com · www.briskfield-exemple.com</p>
    <div class="band"></div>
  </section>
  <span class="option-label" style="left:318px;top:308px">OPTION 2</span>

  <section class="sheet fax-sheet" aria-label="Fax cover sheet">
    <div class="topbar"></div>
    <div class="brand"><span class="dot"></span>BRISK FIELD</div>
    <h1>FAX</h1>
    <div class="fax-fields">
      <div class="fax-field">To:</div><div class="fax-field">From:</div>
      <div class="fax-field">Fax:</div><div class="fax-field">Pages:</div>
      <div class="fax-field">Phone:</div><div class="fax-field">Date:</div>
      <div class="fax-field">Re:</div><div class="fax-field">CC:</div>
    </div>
    <div class="fax-checks"><span>Urgent</span><span>Review</span><span>Comment</span><span>Reply</span><span>Recycle</span></div>
    <div class="fax-rule"></div>
  </section>

  <div class="env env-back-a" aria-label="Envelope back option 1">
    <svg width="230" height="95" viewBox="0 0 230 95"><path d="M0 0 L115 55 L230 0 Z" fill="#1f1f1f"/></svg>
    <div class="brand light"><span class="dot"></span>BRISK FIELD</div>
  </div>
  <div class="env env-front env-front-a" aria-label="Envelope front option 1">
    <div class="brand"><span class="dot"></span>BRISK FIELD</div>
    <p class="address">Tomas Kerbrune<br>7 Rue Montaleur, Res. Les Pins<br>Vallombre</p>
    <div class="band"></div>
  </div>
  <span class="option-label opt-a">OPTION 1</span>

  <div class="env env-back-b" aria-label="Envelope back option 2">
    <svg width="230" height="95" viewBox="0 0 230 95"><path d="M0 0 L115 55 L230 0 Z" fill="#5a0d0d"/></svg>
    <div class="brand light"><span class="dot"></span>BRISK FIELD</div>
  </div>
  <div class="env env-front env-front-b" aria-label="Envelope front option 2">
    <div class="brand"><span class="dot"></span>BRISK FIELD</div>
    <p class="address">Tomas Kerbrune<br>7 Rue Montaleur, Res. Les Pins<br>Vallombre</p>
    <div class="band"></div>
  </div>
  <span class="option-label opt-b">OPTION 2</span>

  <div class="card card-grey"><div class="brand light"><span class="dot"></span>BRISK FIELD</div><p class="details">www.briskfield-exemple.com</p></div>
  <div class="card card-white"><div class="stripe"></div><div class="brand"><span class="dot"></span>BRISK FIELD</div><p class="details">Tomas Kerbrune<br>info@briskfield-exemple.com</p></div>
  <div class="card card-red"><div class="brand light"><span class="dot"></span>BRISK FIELD</div></div>
  <div class="card card-dark"><div class="brand"><span class="dot"></span>BRISK FIELD</div><p class="details">Tomas Kerbrune<br>7 Rue Montaleur, Vallombre</p></div>

</main>
</body>
</html>
```